we need a business card design for a professional painting business. This company has been up and going for about ten years. However it needs an new logo. we want this business card to be modern eye catching and easy to read. I currently have been looking for VC logos but can not find one that suits our needs. This Design should be Our start to a new beginning.
Industry/Entity Type
Painting
Contact Information for Business Card
Varetti Coatings Inc.
Licensed & Insured
Tomas Varetti
Phone(631)384-4562
Fax (555) 730-2418
E-mail varetticoatingsinc@mailbox.example
Requirements
Must have
- a new logo with  VC and i would like it to be in black and white.
i would also like the front to be a solid black with the logo only and then the back to have the information.

```html
<!DOCTYPE html>
<html lang="en">
<head>
<meta charset="utf-8">
<title>Varetti Coatings Inc. — Business Card</title>
<link rel="stylesheet" href="https://fonts.googleapis.com/css2?family=Lato:wght@300;400;700;900&display=swap">
<style>
  :root {
    --backdrop: #2b2b2b;
    --card-black: #050505;
    --ink-white: #ffffff;
    --ink-soft: #e6e6e6;
    --splash-tone: #efefef;
  }
  * { box-sizing: border-box; margin: 0; padding: 0; }
  html, body {
    width: 1200px; height: 900px; overflow: hidden;
    background: var(--backdrop);
    font-family: "Lato", sans-serif;
    color: var(--ink-white);
  }
  .canvas {
    position: relative; width: 1200px; height: 900px;
    display: flex; flex-direction: column; align-items: center; justify-content: center; gap: 48px;
  }
  .card {
    position: relative; width: 660px; height: 377px;
    background: var(--card-black);
    overflow: hidden;
    box-shadow: 0 12px 30px rgba(0,0,0,0.55);
    display: flex; flex-direction: column; align-items: center; justify-content: center;
    text-align: center;
  }
  .splash {
    position: absolute; width: 118px; height: 62px;
    background: var(--splash-tone);
    border-radius: 4px;
  }
  .splash--tl { top: 0; left: 0; border-radius: 0 0 28px 0; }
  .splash--tr { top: 0; right: 0; border-radius: 0 0 0 28px; }
  .splash--bl { bottom: 0; left: 0; border-radius: 0 28px 0 0; }
  .splash--br { bottom: 0; right: 0; border-radius: 28px 0 0 0; }
  .splash--ml { top: 150px; left: 0; width: 92px; border-radius: 0 24px 24px 0; }
  .splash--mr { top: 120px; right: 0; width: 96px; border-radius: 24px 0 0 24px; }

  .brand-mark {
    width: 92px; height: 92px; border-radius: 50%;
    background: var(--ink-white);
    display: flex; align-items: center; justify-content: center;
    margin-bottom: 20px;
  }
  .brand-initials {
    font-weight: 900; font-size: 42px; letter-spacing: 1px;
    color: var(--card-black); line-height: 1;
  }
  .brand-name {
    font-weight: 900; font-size: 36px; letter-spacing: 2px;
    text-transform: uppercase; color: var(--ink-white);
  }
  .brand-tagline {
    font-weight: 300; font-size: 24px; letter-spacing: 0.5px;
    color: var(--ink-soft); margin-top: 6px;
  }

  .card--back .brand-mark { width: 96px; height: 96px; margin-bottom: 28px; }
  .card--back .brand-initials { font-size: 44px; }
  .person-name {
    font-weight: 700; font-size: 24px; letter-spacing: 2px;
    text-transform: uppercase; margin-bottom: 18px;
  }
  .contact-list { list-style: none; font-size: 18px; line-height: 1.55; font-weight: 400; }
  .contact-list .label { font-weight: 700; }
</style>
</head>
<body>
<main class="canvas">
  <section class="card card--front">
    <div class="splash splash--tr" role="img" aria-label="White paint splatter"></div>
    <div class="splash splash--ml" role="img" aria-label="White paint splatter"></div>
    <div class="splash splash--mr" role="img" aria-label="White paint splatter"></div>
    <div class="splash splash--bl" role="img" aria-label="White paint splatter"></div>
    <div class="brand-mark"><span class="brand-initials">VC</span></div>
    <h1 class="brand-name">Varetti Coatings Inc.</h1>
    <p class="brand-tagline">Licensed &amp; Insured</p>
  </section>

  <section class="card card--back">
    <div class="splash splash--tl" role="img" aria-label="White paint splatter"></div>
    <div class="splash splash--tr" role="img" aria-label="White paint splatter"></div>
    <div class="splash splash--bl" role="img" aria-label="White paint splatter"></div>
    <div class="splash splash--br" role="img" aria-label="White paint splatter"></div>
    <div class="brand-mark"><span class="brand-initials">VC</span></div>
    <h2 class="person-name">Tomas Varetti</h2>
    <ul class="contact-list">
      <li><span class="label">Telephone:</span> (555)217-8093</li>
      <li><span class="label">Fax:</span> (555) 730-2418</li>
      <li><span class="label">Email:</span> varetticoatingsinc@mailbox.example</li>
    </ul>
  </section>
</main>
</body>
</html>
```